Business Card Design - PathwayMinds

Looking for creative, modern design, two sided for PathwayMinds that is consistent with color and feel of website www.pathwayminds.example.
Updates

Back of card will be used to promote products or have a quote revolving around decisions, change, leadership, innovation, creativity. Back should also have space to promote website, but optional to use the icon. Front of the card will need to use the icon and have standard place for name, job title, phone and email. We are not looking to put a mailing address or fax. Also want space to place a few words/phrase explaining what we do...such as individual growth and organizational development or tools, training, information...in addition, want the chatterbook icon small on the front somewhere as we are also on chatterbook.

Vector file uploaded of icon.

Target Market(s)

Professional coaching for individual growth and organizational development

Industry/Entity Type

Business

Requirements
Must have
• Icon...see attached.

```html
<!DOCTYPE html>
<html lang="en">
<head>
<meta charset="utf-8">
<title>PathwayMinds – Business Card Set</title>
<link rel="stylesheet" href="https://fonts.googleapis.com/css2?family=Open+Sans:wght@400;600;700&display=swap">
<style>
  :root {
    --backdrop: #3b3b3d;
    --navy-deep: #1d4382;
    --navy-mid: #2a5599;
    --paper: #e7eaf0;
    --paper-shade: #d6dce8;
    --ink-navy: #1e3a6e;
    --white: #ffffff;
    --mark-blue: #3d8fd8;
    --mark-light: #9fc6ec;
  }
  * { margin: 0; padding: 0; box-sizing: border-box; }
  html, body {
    width: 1200px; height: 900px; overflow: hidden;
    background: var(--backdrop);
    font-family: "Open Sans", sans-serif;
  }
  .canvas { position: relative; width: 1200px; height: 900px; }
  .card {
    position: absolute; width: 525px; height: 300px; overflow: hidden;
  }
  .card--dark { background: linear-gradient(135deg, var(--navy-mid), var(--navy-deep)); color: var(--white); }
  .card--light { background: linear-gradient(135deg, #eef1f5, var(--paper)); color: var(--ink-navy); }
  .card--back-intro { left: 58px; top: 131px; }
  .card--back-motto { left: 617px; top: 131px; }
  .card--back-large { left: 58px; top: 471px; }
  .card--front { left: 617px; top: 471px; }

  .decor {
    position: absolute; border-radius: 50%;
  }
  .decor--dark { background: radial-gradient(circle, rgba(120,160,220,0.18), rgba(120,160,220,0) 70%); }
  .decor--light { background: radial-gradient(circle, rgba(160,180,215,0.45), rgba(160,180,215,0) 70%); }

  .mark-dot {
    position: absolute; border-radius: 50%;
    background: radial-gradient(circle at 40% 35%, var(--mark-light), var(--mark-blue));
  }

  .brand-name { position: absolute; font-weight: 400; letter-spacing: -0.5px; white-space: nowrap; line-height: 1; }
  .line { position: absolute; white-space: nowrap; line-height: 1.2; }
  .right { text-align: right; }
  .motto { font-weight: 400; }

  .contact-row { display: flex; align-items: center; gap: 6px; }
  .badge {
    display: inline-flex; align-items: center; justify-content: center;
    width: 16px; height: 16px; border-radius: 3px;
    background: var(--white); color: var(--navy-deep);
    font-size: 12px; font-weight: 700; line-height: 1;
  }
  .badge--plain { font-size: 0; }
</style>
</head>
<body>
<main class="canvas">

  <!-- Back: intro statement -->
  <section class="card card--dark card--back-intro">
    <div class="decor decor--dark" role="img" aria-label="Faint large brand graphic" style="left:10px;top:-40px;width:300px;height:380px;"></div>
    <div class="mark-dot" style="left:55px;top:80px;width:140px;height:140px;"></div>
    <h2 class="brand-name" style="left:224px;top:124px;font-size:38px;">PathwayMinds</h2>
    <p class="line right" style="right:58px;top:162px;font-size:13px;">www.pathwayminds.example</p>
    <p class="line" style="left:224px;top:207px;font-size:11.5px;">Providing tools, training, information and<br>collaboration to achieve the results you want.</p>
  </section>

  <!-- Back: motto with mark -->
  <section class="card card--light card--back-motto">
    <div class="decor decor--light" role="img" aria-label="Faint large brand graphic" style="left:-20px;top:-30px;width:260px;height:360px;"></div>
    <div class="mark-dot" style="left:63px;top:75px;width:130px;height:130px;"></div>
    <h2 class="brand-name right" style="right:58px;top:107px;font-size:38px;">PathwayMinds</h2>
    <p class="line right motto" style="right:58px;top:152px;font-size:22px;">“Design Your Life”</p>
    <p class="line right" style="right:58px;top:187px;font-size:14px;">www.pathwayminds.example</p>
  </section>

  <!-- Back: large motto -->
  <section class="card card--light card--back-large">
    <div class="decor decor--light" role="img" aria-label="Large faint brand graphic area" style="left:-60px;top:-40px;width:360px;height:380px;"></div>
    <h2 class="brand-name right" style="right:58px;top:100px;font-size:42px;">PathwayMinds</h2>
    <p class="line right motto" style="right:58px;top:148px;font-size:24px;">“Design Your Life”</p>
    <p class="line right" style="right:58px;top:186px;font-size:15px;">www.pathwayminds.example</p>
  </section>

  <!-- Front: contact details -->
  <section class="card card--dark card--front">
    <div class="decor decor--dark" role="img" aria-label="Faint large brand graphic" style="left:230px;top:-20px;width:320px;height:340px;"></div>
    <div class="mark-dot" style="left:45px;top:53px;width:76px;height:76px;"></div>
    <h2 class="brand-name" style="left:138px;top:71px;font-size:30px;">PathwayMinds</h2>
    <p class="line" style="left:139px;top:101px;font-size:11px;">Supporting Individual Growth &amp; Organizational Development</p>

    <p class="line" style="left:55px;top:196px;font-size:18px;font-weight:700;">Marcus Ellery</p>
    <p class="line" style="left:55px;top:214px;font-size:14px;">Position</p>
    <p class="line contact-row" style="left:55px;top:238px;font-size:15px;"><span class="badge badge--plain"></span>/pathwayminds</p>

    <div class="line" style="left:262px;top:197px;font-size:15px;line-height:21px;">
      <p class="contact-row"><span class="badge">p</span>1.800.555.0142</p>
      <p class="contact-row"><span class="badge">e</span>contact@pathwayminds.example</p>
      <p class="contact-row"><span class="badge">w</span>www.pathwayminds.example</p>
    </div>
  </section>

</main>
</body>
</html>
```